Web Site Redesign

We operate a data centre facility specialing in colocation and Fibre optic connectivity (i.e. point to point fibre services and internet over fibre).

We have an existing site located at www.corvanlink.example however this is very very tired and requires a redesign. We are looking for a fresh new design that will be appealing to potential customers.

The Company name is Corvan Lk and the primary corporate colour is bright red with secondary colours of white, grey and black. Specific bright red can be seen in attached company logo.

Website needs to be modern, clean and professional representing our premium colocation and fibre provider branding.

Our company slogan is : safe. secure. reliable

We will provide feedback regardless of the quality of the design to ensure a better outcome for all parties.

Please feel free to contact us if you have any questions.

# The designer can use placeholder images or feel free to use any/all or none of the attached images
# The designer can use sample filler text

Target Market(s)

Technical IT Professionals as well C level executives (i.e. CEO's, CIO).

Industry/Entity Type

Internet

Requirements
Must have
• clean design
Nice to have
• A sidebar with two sections. 1 for current promo and 1 for "Let us call you back/contact you"
Should not have
• Clutter

```html
<!DOCTYPE html>
<html lang="en">
<head>
<meta charset="utf-8">
<title>Corvan Lk – Data Centre</title>
<link href="https://fonts.googleapis.com/css2?family=Arimo:wght@400;700&display=swap" rel="stylesheet">
<style>
:root{
  --red:#e0302f;
  --red-dark:#c21f1f;
  --ink:#222;
  --text:#555;
  --muted:#8a8a8a;
  --page:#f7f7f7;
  --band:#5a5a5a;
  --nav-top:#3c3c3c;
  --nav-bottom:#111;
  --footer:#262626;
  --footer-panel:#3a3a3a;
}
*{margin:0;padding:0;box-sizing:border-box}
html,body{width:1108px;height:1200px;overflow:hidden;background:var(--page)}
body{font-family:"Arimo",Arial,sans-serif;color:var(--text)}
.site{position:relative;width:1200px;height:1300px;transform:scale(0.92333);transform-origin:0 0;background:var(--page);overflow:hidden}
.abs{position:absolute}
.top-strip{left:0;top:0;width:1200px;height:8px;background:var(--red)}
.login-tab{left:932px;top:0;width:167px;height:36px;background:var(--red);border-radius:0 0 4px 4px;color:#fff;font-size:11px;font-weight:700;text-align:center;line-height:34px;letter-spacing:.3px}
.brand{left:132px;top:120px;display:flex;align-items:center;gap:10px;font-size:34px;color:var(--ink)}
.brand-mark{width:22px;height:22px;background:var(--red)}
.search{left:787px;top:123px;width:290px;height:32px;background:#e2e3ea;border:1px solid #c9c9cf;border-radius:3px;box-shadow:inset 0 2px 3px rgba(0,0,0,.15)}
.search span{position:absolute;left:23px;top:8px;font-size:12px;color:#444}
.search .btn{position:absolute;right:0;top:0;width:41px;height:30px;border-left:2px solid #777;background:#f2f2f2}
.head-band{left:0;top:212px;width:1200px;height:65px;background:linear-gradient(#dedede,#f3f3f3 60%,#fafafa)}
.nav{left:102px;top:188px;width:998px;height:46px;border-radius:4px;background:linear-gradient(var(--nav-top),var(--nav-bottom));box-shadow:0 6px 8px -4px rgba(0,0,0,.4)}
.nav a{position:absolute;top:15px;color:#fff;font-size:12px;font-weight:700;text-decoration:none;letter-spacing:.2px}
.nav a.current{color:var(--red);background:#454545;top:9px;height:26px;line-height:26px;padding:0 22px;left:17px}
.hero-band{left:0;top:277px;width:1200px;height:285px;background:var(--band)}
.slider{left:100px;top:290px;width:1000px;height:337px;background:#fff;border:1px solid #ddd}
.slide-photo{left:104px;top:294px;width:590px;height:329px;background:linear-gradient(90deg,#1a1a1a 0%,#2b2d30 40%,#6c7378 75%,#d9dadb 92%,#fff 100%)}
.caption-bar{left:104px;top:582px;width:560px;height:41px;background:linear-gradient(90deg,rgba(0,0,0,.55),rgba(0,0,0,.35) 80%,rgba(0,0,0,0))}
.slogan{left:160px;top:589px;color:#fff;font-size:22px;letter-spacing:1.5px}
.slide-title{left:712px;top:316px;color:var(--red);font-size:23px}
.slide-copy{left:713px;top:383px;width:355px;font-size:12px;line-height:22px;color:#444}
.learn-btn{left:883px;top:516px;width:178px;height:41px;background:linear-gradient(#ee4242,var(--red-dark));border-radius:6px;color:#fff;font-size:18px;line-height:40px;padding-left:20px;letter-spacing:.5px}
.learn-btn svg{position:absolute;right:22px;top:13px}
.slide-arrow{top:419px;width:43px;height:52px;background:#fff;border-radius:4px;box-shadow:0 1px 4px rgba(0,0,0,.3)}
.slide-arrow svg{position:absolute;left:13px;top:17px}
.slider-shadow{left:350px;top:626px;width:520px;height:10px;border-radius:50%;background:radial-gradient(rgba(0,0,0,.35),rgba(0,0,0,0) 70%)}
.welcome-title{left:117px;top:650px;font-size:20px;color:#666}
.welcome-copy{left:116px;top:688px;width:715px;font-size:12px;line-height:14px;color:#555}
.welcome-copy p{margin-bottom:14px}
.welcome-copy p:first-child{padding-left:4px}
.welcome-photo{left:843px;top:658px;width:254px;height:170px;border:1px solid #999;background:#fff;padding:4px}
.welcome-photo div{width:100%;height:100%;background:linear-gradient(135deg,#c9c4bb,#8e8a84 45%,#3b3b3d 70%,#9a5a44)}
.step-num{width:58px;height:58px;border-radius:50%;background:var(--ink);color:#fff;font-size:40px;text-align:center;line-height:58px;top:841px}
.step-title{top:848px;font-size:30px;color:var(--ink)}
.step-rule{top:886px;height:6px;background:radial-gradient(ellipse at center,#bdbdbd,rgba(190,190,190,0) 72%)}
.step-copy{top:905px;width:320px;font-size:12px;line-height:18px;color:var(--muted)}
.read-more{top:1000px;height:31px;border-radius:16px;background:linear-gradient(#fbfbfb,#dcdcdc);box-shadow:0 1px 3px rgba(0,0,0,.3);font-size:13px;font-weight:700;color:#444;line-height:31px;padding:0 20px}
.section-rule{left:100px;top:1058px;width:1005px;height:8px;background:radial-gradient(ellipse at center,#c4c4c4,rgba(200,200,200,0) 72%)}
.partners-title{left:104px;top:1080px;font-size:18px;color:var(--ink)}
.footer-base{left:0;top:1240px;width:1200px;height:60px;background:var(--footer)}
.footer-panel{left:100px;top:1227px;width:1001px;height:73px;background:var(--footer-panel)}
.footer-links{top:1242px;font-size:12px;color:#ccc}
.copyright{left:497px;top:1272px;font-size:12px;color:#aaa}
.social{top:1273px;width:22px;height:22px;border-radius:3px}
</style>
</head>
<body>
<div class="site">
  <div class="abs top-strip"></div>
  <div class="abs login-tab">LOGIN / SIGN UP</div>
  <div class="abs brand"><span class="brand-mark"></span><span>Corvan Lk</span></div>
  <div class="abs search"><span>search</span>
    <div class="btn"><svg width="41" height="30" viewBox="0 0 41 30"><circle cx="18" cy="13" r="7" fill="none" stroke="#111" stroke-width="3"/><line x1="23" y1="18" x2="28" y2="24" stroke="#111" stroke-width="4" stroke-linecap="round"/></svg></div>
  </div>

  <div class="abs head-band"></div>
  <nav class="abs nav">
    <a class="current" href="#">HOME</a>
    <a style="left:128px" href="#">ABOUT US</a>
    <a style="left:232px" href="#">FACILITIES</a>
    <a style="left:351px" href="#">BUSINESS CONTINUITY</a>
    <a style="left:551px" href="#">SERVICES</a>
    <a style="left:663px" href="#">PARTNERS</a>
    <a style="left:780px" href="#">WEBMAIL</a>
    <a style="left:887px" href="#">CONTACT US</a>
  </nav>

  <div class="abs hero-band"></div>
  <div class="abs slider"></div>
  <div class="abs slide-photo" role="img" aria-label="Rows of server racks in a data centre aisle"></div>
  <div class="abs caption-bar"></div>
  <div class="abs slogan">safe.&nbsp; secure. reliable.</div>
  <div class="abs slide-title">Lorem ipsum dolor sit amet,</div>
  <div class="abs slide-copy">Lorem ipsum dolor sit amet, consectetuer adipiscing elit. Aenean commodo ligula eget dolor. Aenean massa. Cum sociis natoque penatibus et magnis dis parturient montes, nascetur ridiculus mus.</div>
  <div class="abs learn-btn">Learn more
    <svg width="18" height="14" viewBox="0 0 18 14"><path d="M2 1l6 6-6 6M9 1l6 6-6 6" fill="none" stroke="#fff" stroke-width="2.6"/></svg>
  </div>
  <div class="abs slide-arrow" style="left:93px"><svg width="16" height="18" viewBox="0 0 16 18"><path d="M12 2L5 9l7 7" fill="none" stroke="#111" stroke-width="4"/></svg></div>
  <div class="abs slide-arrow" style="left:1065px"><svg width="16" height="18" viewBox="0 0 16 18"><path d="M4 2l7 7-7 7" fill="none" stroke="#c21f1f" stroke-width="4"/></svg></div>
  <div class="abs slider-shadow"></div>

  <h1 class="abs welcome-title" style="font-weight:400">Welcome to Corvan Lk</h1>
  <div class="abs welcome-copy">
    <p>A world class data centre in the safest place on Earth.</p>
    <p>With a centrally located data centre in the heart of the Harbourview CBD Corvan Lk is excellently positioned to assist with your critical IT requirements.</p>
    <p>The CBD facility features overlapping power grids, redundant power supplies and comprehensively maintained infrastructure, providing excellent levels of protection for your critical IT equipment. The State's newest and most technologically advanced data centre is also now open in Eastmere, a convenient 5.5 km's from the CBD providing a perfect location for either production sites, or DR infrastructure.</p>
  </div>
  <div class="abs welcome-photo"><div role="img" aria-label="Professional working on a laptop while seated on outdoor steps"></div></div>

  <div class="abs step-num" style="left:105px">1</div>
  <div class="abs step-title" style="left:293px">WHY ?</div>
  <div class="abs step-rule" style="left:90px;width:340px"></div>
  <div class="abs step-copy" style="left:104px">Lorem ipsum dolor sit amet, consectetuer adipiscing elit. Aenean commodo ligula eget dolor. Aenean massa. Cum sociis natoque penatibus et magnis dis parturient montes, nascetur ridiculus mus.</div>
  <div class="abs read-more" style="left:296px">Read more »</div>

  <div class="abs step-num" style="left:446px">2</div>
  <div class="abs step-title" style="left:604px">WHERE ?</div>
  <div class="abs step-rule" style="left:432px;width:340px"></div>
  <div class="abs step-copy" style="left:446px">Lorem ipsum dolor sit amet, consectetuer adipiscing elit. Aenean commodo ligula eget dolor. Aenean massa. Cum sociis natoque penatibus et magnis dis parturient montes, nascetur ridiculus mus.</div>
  <div class="abs read-more" style="left:653px">Read more »</div>

  <div class="abs step-num" style="left:787px">3</div>
  <div class="abs step-title" style="left:987px">HOW ?</div>
  <div class="abs step-rule" style="left:772px;width:340px"></div>
  <div class="abs step-copy" style="left:790px">Lorem ipsum dolor sit amet, consectetuer adipiscing elit. Aenean commodo ligula eget dolor. Aenean massa. Cum sociis natoque penatibus et magnis dis parturient montes, nascetur ridiculus mus.</div>
  <div class="abs read-more" style="left:1004px">Read more »</div>

  <div class="abs section-rule"></div>
  <h2 class="abs partners-title" style="font-weight:400">Partners</h2>
  <svg class="abs" style="left:114px;top:1125px" width="22" height="28" viewBox="0 0 22 28"><path d="M17 3L6 14l11 11" fill="none" stroke="#111" stroke-width="5"/></svg>
  <svg class="abs" style="left:1064px;top:1125px" width="22" height="28" viewBox="0 0 22 28"><path d="M5 3l11 11-11 11" fill="none" stroke="#111" stroke-width="5"/></svg>

  <div class="abs footer-base"></div>
  <footer class="abs footer-panel"></footer>
  <div class="abs footer-links" style="left:183px">Home</div>
  <div class="abs footer-links" style="left:245px">|</div>
  <div class="abs footer-links" style="left:273px">About Us</div>
  <div class="abs footer-links" style="left:345px">|</div>
  <div class="abs footer-links" style="left:372px">Facilities</div>
  <div class="abs footer-links" style="left:442px">|</div>
  <div class="abs footer-links" style="left:472px">Business Continuity</div>
  <div class="abs footer-links" style="left:606px">|</div>
  <div class="abs footer-links" style="left:645px">Services</div>
  <div class="abs footer-links" style="left:715px">|</div>
  <div class="abs footer-links" style="left:746px">Partners</div>
  <div class="abs footer-links" style="left:824px">|</div>
  <div class="abs footer-links" style="left:848px">Webmail</div>
  <div class="abs footer-links" style="left:923px">|</div>
  <div class="abs footer-links" style="left:946px">Contact Us</div>
  <div class="abs copyright">© 2010 Corvan Lk All rights reserved</div>
  <div class="abs social" style="left:970px;background:#5fb8de"></div>
  <div class="abs social" style="left:1012px;background:#e8822a"></div>
  <div class="abs social" style="left:1055px;background:#4a6aad"></div>
</div>
</body>
</html>
```